Counseling Practice Business Card

I need a professional looking business card incorporating my new logo that was just completed. Card needs to incorporate my name and title, description of my specialty, my address, my phone number, my fax number, my email and my website URL. I need to be able to choose design on/with different paper colors and textures.
I do not have a lot of business card ideas so I am open to anything but I want bold,sharp, clear card without additional designs other than my logo (see attached file info). I am open to different color backgrounds or paper colors including black. I do not like traditional brackets around area codes in phone number or dashes between numbers in phone number. Am open to other ways of presenting including periods between numbers as appropriate. I do not know enough to know what I like yet but I want card to coordinate and work together with my logo. My practice emphasizes natural mental health interventions so any use of color (with background paper color or the blue and green in my logo) that elicits nature is nice. In addition to black, any natural brown or wood looking background might be desirable also. Most of the offerings so far look very similar and boring.

Target Market(s)

Potential therapy clients and other professionals

Contact Information for Business Card

Card information:
Marcus T. Whitfield, Ph.D.
Licensed Clinical Psychologist
Integrative Health Coach
4812 Ferndale Pkwy NW
Suite 730
Larkston, GA 30412
(770) 555-0142 phone
(770) 555-0186 fax
drmarcuswhitfield@kelvora.com
pathbloomcounseling.com

Font styles to use
Serif
Sans Serif
Other font styles liked:
• anything that you think looks crisp, clear and easily readable

Requirements
Must have
• Any color used should coordinate with my logo design (see attached files).
• Card should be printed horizontally so top and bottom are longest sides of rectangle.
• Background color or paper color should complement and highlight logo. Do not like a white background. black, grey, brown or any color my logo would blend well with.
Nice to have
• I would like designer to utilize color to highlight letters/name or phone-fax-web symbols.
• Bottom edge of card could be highlighted if appropriate to an idea.
Should not have
• I would NOT want the card to have a pure white background at all.
• No clear cards.
• Cards should be oriented with long sides on bottom and top, NOT sides. DO NOT LIKE THIS THIN TALL ORIENTATION.

```html
<!DOCTYPE html>
<html lang="en">
<head>
<meta charset="utf-8">
<title>Pathbloom Counseling – Business Cards</title>
<link rel="stylesheet" href="https://fonts.googleapis.com/css2?family=Arimo:wght@700&family=Tinos:wght@700&display=swap">
<style>
  :root{
    --page:#e6e6e4;
    --black:#0b0b0b;
    --charcoal:#202020;
    --charcoal-edge:#2b2b2b;
    --blue:#2f7fe0;
    --deep-blue:#1d2fa6;
    --navy:#1b2a6b;
    --title-grey:#c9cce6;
    --gold:#f6c21c;
    --icon-gold:#f0ad17;
    --paper-light:#e4e4e2;
    --paper-mid:#c9c9c6;
    --paper-fold:#b9b8b4;
    --wood-dark:#3a2012;
    --wood-mid:#5e3a22;
    --white:#ffffff;
    --sans:"Arimo", Arial, sans-serif;
    --serif:"Tinos", "Times New Roman", serif;
  }
  *{box-sizing:border-box;margin:0;padding:0}
  html,body{width:1200px;height:543px;overflow:hidden;background:var(--page)}
  .sheet{position:relative;width:1200px;height:543px;display:flex;gap:26px;justify-content:center;align-items:center}
  .card{position:relative;width:560px;height:302px;overflow:hidden;box-shadow:0 6px 18px rgba(0,0,0,.25)}
  .card__art{position:absolute;inset:0;width:100%;height:100%}
  .card--black{background:var(--black);--icon-bg:var(--blue);--contact:var(--gold);--wordmark:var(--blue);--name:var(--white);--title:var(--title-grey);--contacts-left:262px}
  .card--wood{background:var(--wood-mid);--icon-bg:var(--icon-gold);--contact:var(--gold);--wordmark:var(--deep-blue);--name:var(--deep-blue);--title:var(--navy);--contacts-left:288px}
  .wordmark{position:absolute;left:18px;top:16px;color:var(--wordmark);font-family:var(--sans);font-weight:700;line-height:1}
  .wordmark__name{display:block;font-size:44px;letter-spacing:-.5px}
  .wordmark__tag{display:block;font-size:15px;letter-spacing:7.4px;margin-top:6px;padding-left:4px}
  .identity{position:absolute;left:8px;top:110px}
  .identity__name{font-family:var(--sans);font-weight:700;font-size:17px;color:var(--name)}
  .identity__title{font-family:var(--serif);font-weight:700;font-size:14px;color:var(--title);line-height:17px}
  .identity__name + .identity__title{margin-top:6px}
  .contacts{position:absolute;left:var(--contacts-left);top:124px;list-style:none;font-family:var(--serif);font-weight:700;font-size:15px;color:var(--contact);white-space:nowrap}
  .contacts li{display:flex;align-items:flex-start;gap:6px;line-height:17px;margin-bottom:9px}
  .contacts .contact--address{margin-bottom:10px}
  .contact__icon{flex:0 0 20px;width:20px;height:20px;border-radius:50%;background:var(--icon-bg);display:flex;align-items:center;justify-content:center}
  .contact__icon svg{width:13px;height:13px;fill:var(--white)}
  .contact--address .contact__icon{background:none}
  .contact--address .contact__icon svg{width:20px;height:20px;fill:var(--icon-bg)}
</style>
</head>
<body>
<svg width="0" height="0" style="position:absolute" aria-hidden="true">
  <defs>
    <symbol id="icon-pin" viewBox="0 0 24 24"><path d="M12 1a8 8 0 0 0-8 8c0 6 8 14 8 14s8-8 8-14a8 8 0 0 0-8-8zm0 11a3 3 0 1 1 0-6 3 3 0 0 1 0 6z"/></symbol>
    <symbol id="icon-phone" viewBox="0 0 24 24"><path d="M6.6 10.8a15 15 0 0 0 6.6 6.6l2.2-2.2a1 1 0 0 1 1-.25 11 11 0 0 0 3.6.6 1 1 0 0 1 1 1V20a1 1 0 0 1-1 1A17 17 0 0 1 3 4a1 1 0 0 1 1-1h3.5a1 1 0 0 1 1 1 11 11 0 0 0 .6 3.6 1 1 0 0 1-.25 1z"/></symbol>
    <symbol id="icon-fax" viewBox="0 0 24 24"><path d="M6 2h12v5H6zM3 8h18a1 1 0 0 1 1 1v8h-4v5H6v-5H2V9a1 1 0 0 1 1-1zm5 8v4h8v-4z"/></symbol>
    <symbol id="icon-mail" viewBox="0 0 24 24"><path d="M2 5h20v14H2zm2 2v.5l8 5.5 8-5.5V7zm0 3v7h16v-7l-8 5.5z"/></symbol>
    <symbol id="icon-web" viewBox="0 0 24 24"><path d="M12 2a10 10 0 1 0 0 20 10 10 0 0 0 0-20zm7.9 9h-3.4a15 15 0 0 0-1.6-6.5A8 8 0 0 1 19.9 11zM12 4c1 1.2 2.3 3.7 2.5 7h-5C9.7 7.7 11 5.2 12 4zM9.1 4.5A15 15 0 0 0 7.5 11H4.1a8 8 0 0 1 5-6.5zM4.1 13h3.4a15 15 0 0 0 1.6 6.5 8 8 0 0 1-5-6.5zM12 20c-1-1.2-2.3-3.7-2.5-7h5c-.2 3.3-1.5 5.8-2.5 7zm2.9-.5a15 15 0 0 0 1.6-6.5h3.4a8 8 0 0 1-5 6.5z"/></symbol>
  </defs>
</svg>

<main class="sheet">
  <!-- Black card -->
  <section class="card card--black">
    <svg class="card__art" viewBox="0 0 560 302" preserveAspectRatio="none" aria-hidden="true">
      <polygon points="0,0 340,0 118,302 0,302" fill="var(--charcoal)"/>
      <polygon points="0,0 340,0 330,14 0,14" fill="var(--charcoal-edge)" opacity=".5"/>
      <polygon points="340,0 120,274 190,236" fill="var(--blue)"/>
    </svg>
    <div class="wordmark"><span class="wordmark__name">Pathbloom</span><span class="wordmark__tag">COUNSELING</span></div>
    <div class="identity">
      <p class="identity__name">Marcus T. Whitfield, Ph.D.</p>
      <p class="identity__title">Licensed Clinical Psychologist</p>
      <p class="identity__title">Integrative Health Coach</p>
    </div>
    <ul class="contacts">
      <li class="contact--address"><span class="contact__icon"><svg><use href="#icon-pin"/></svg></span><span>4812 Ferndale Pkwy NW,<br>Suite 730, Larkston,<br>GA 30412.</span></li>
      <li><span class="contact__icon"><svg><use href="#icon-phone"/></svg></span><span>(770) 555-0142</span></li>
      <li><span class="contact__icon"><svg><use href="#icon-fax"/></svg></span><span>(770) 555-0186</span></li>
      <li><span class="contact__icon"><svg><use href="#icon-mail"/></svg></span><span>drmarcuswhitfield@kelvora.com</span></li>
      <li><span class="contact__icon"><svg><use href="#icon-web"/></svg></span><span>pathbloomcounseling.com</span></li>
    </ul>
  </section>

  <!-- Wood and paper card -->
  <section class="card card--wood">
    <svg class="card__art" viewBox="0 0 560 302" preserveAspectRatio="none">
      <defs>
        <linearGradient id="wood-tone" x1="0" y1="0" x2="1" y2="1">
          <stop offset="0" stop-color="var(--wood-mid)"/>
          <stop offset="1" stop-color="var(--wood-dark)"/>
        </linearGradient>
        <linearGradient id="paper-tone" x1="0" y1="0" x2="1" y2="1">
          <stop offset="0" stop-color="var(--paper-light)"/>
          <stop offset="1" stop-color="var(--paper-mid)"/>
        </linearGradient>
      </defs>
      <rect width="560" height="302" fill="url(#wood-tone)" role="img" aria-label="Dark brown wood grain background"/>
      <polygon points="0,0 322,0 222,302 0,302" fill="url(#paper-tone)" role="img" aria-label="Crumpled off-white paper texture"/>
      <polygon points="322,0 252,140 282,60" fill="var(--paper-fold)" aria-hidden="true"/>
    </svg>
    <div class="wordmark"><span class="wordmark__name">Pathbloom</span><span class="wordmark__tag">COUNSELING</span></div>
    <div class="identity">
      <p class="identity__name">Marcus T. Whitfield, Ph.D.</p>
      <p class="identity__title">Licensed Clinical Psychologist</p>
      <p class="identity__title">Integrative Health Coach</p>
    </div>
    <ul class="contacts">
      <li class="contact--address"><span class="contact__icon"><svg><use href="#icon-pin"/></svg></span><span>4812 Ferndale Pkwy NW,<br>Suite 730, Larkston,<br>GA 30412.</span></li>
      <li><span class="contact__icon"><svg><use href="#icon-phone"/></svg></span><span>(770) 555-0142</span></li>
      <li><span class="contact__icon"><svg><use href="#icon-fax"/></svg></span><span>(770) 555-0186</span></li>
      <li><span class="contact__icon"><svg><use href="#icon-mail"/></svg></span><span>drmarcuswhitfield@kelvora.com</span></li>
      <li><span class="contact__icon"><svg><use href="#icon-web"/></svg></span><span>pathbloomcounseling.com</span></li>
    </ul>
  </section>
</main>
</body>
</html>
```